ZAMO needs a beautiful/corp web page

We are a pump an compressor repair facility in Alberta Canada. We love clean looks. white yellows greens blues. main page should involve conola fields, sun shine

Reason: i will be guaranteeing the project keep up the good work

Requirements
Must have
• open conola fields

```html
<!DOCTYPE html>
<html lang="en">
<head>
<meta charset="utf-8">
<title>ZAMO Rotating Solutions</title>
<link href="https://fonts.googleapis.com/css2?family=Didact+Gothic&family=Mulish:ital,wght@0,700;1,400&family=Questrial&display=swap" rel="stylesheet">
<style>
:root{
  --sky:#3f6fb3;
  --sky-light:#a9c4e4;
  --canola:#e8d53a;
  --canola-deep:#c9b21c;
  --field-green:#6b7a2a;
  --card:rgba(250,250,235,.86);
  --ink:#2a2a2a;
  --nav:#2b2a2a;
  --orange:#e8861f;
  --overlay:rgba(58,56,18,.78);
  --white:#ffffff;
}
*{margin:0;padding:0;box-sizing:border-box}
html,body{width:1108px;height:1200px;overflow:hidden}
body{position:relative;font-family:"Didact Gothic",sans-serif;color:var(--ink);
  background:linear-gradient(180deg,var(--sky) 0%,var(--sky-light) 28%,#c9cf8a 42%,var(--canola) 55%,var(--canola-deep) 80%,var(--field-green) 100%)}
.backdrop{position:absolute;inset:0}
.page-card{position:absolute;left:55px;top:60px;width:997px;height:1080px;border-radius:56px;overflow:hidden;
  background:var(--card);box-shadow:0 4px 14px rgba(0,0,0,.3)}
.card-top{position:absolute;left:0;top:0;width:100%;height:97px;background:rgba(240,242,246,.9)}
.hero{position:absolute;left:0;top:97px;width:100%;height:563px;
  background:linear-gradient(180deg,#4f82c4 0%,#cfdcec 30%,#eef2f4 45%,#6f8a3a 51%,#ecdc3e 54%,#e2cf2a 80%,#c8b520 100%)}
.logo-box{position:absolute;left:106px;top:26px;width:263px;height:263px;background:var(--white);border-radius:12px;
  box-shadow:0 2px 8px rgba(0,0,0,.35);display:flex;flex-direction:column;align-items:center;justify-content:flex-end;padding-bottom:22px}
.logo-mark{width:20px;height:20px;border-radius:50%;background:var(--orange);margin-bottom:14px}
.logo-name{font-family:"Mulish",sans-serif;font-weight:700;font-size:66px;line-height:1;color:var(--ink);letter-spacing:2px}
.logo-tag{font-family:"Questrial",sans-serif;font-size:21px;color:var(--ink);margin-top:6px}
.contact{position:absolute;top:98px;font-family:"Questrial",sans-serif;font-size:18px;color:#333;display:flex;align-items:center;gap:6px}
.contact.phone{left:407px}
.contact.email{right:107px;font-size:17px}
.main-nav{position:absolute;left:408px;top:127px;width:600px;height:60px;background:var(--nav);border-radius:8px;
  box-shadow:0 2px 6px rgba(0,0,0,.4);display:flex;align-items:center;justify-content:space-between;padding:0 10px 0 12px}
.main-nav a{font-family:"Questrial",sans-serif;font-size:25px;color:var(--white);text-decoration:none}
.main-nav a.active{font-weight:700;font-family:"Mulish",sans-serif}
.mission{position:absolute;left:585px;top:355px;width:377px;height:133px;background:var(--overlay);padding:16px 16px 0 14px;color:var(--white)}
.mission p{font-family:"Mulish",sans-serif;font-style:italic;font-size:16px;line-height:20px;text-align:justify;text-indent:34px}
.mission .more{position:absolute;right:16px;bottom:10px;font-size:12px}
.search{position:absolute;left:585px;top:503px;display:flex;height:38px}
.search input{width:266px;height:38px;border:1px solid #ccc;padding:0 14px;font-family:"Didact Gothic",sans-serif;font-size:15px;color:#777;background:var(--white)}
.search button{width:111px;height:38px;border:0;background:var(--orange);color:var(--white);font-family:"Didact Gothic",sans-serif;font-size:23px}
.welcome{position:absolute;left:30px;top:625px;width:447px;height:420px}
h2{font-family:"Mulish",sans-serif;font-weight:700;color:var(--ink)}
.welcome h2{font-size:22px;margin-bottom:22px}
.welcome p{font-size:17.4px;line-height:20px;text-align:justify;text-indent:33px}
.see-more{position:absolute;font-size:13px}
.welcome .see-more{right:0;top:392px}
.product-photo{position:absolute;left:490px;top:620px;width:212px;height:212px;background:var(--white);border-radius:6px;
  box-shadow:0 2px 6px rgba(0,0,0,.35);padding:12px}
.product-photo div{width:100%;height:100%;border-radius:4px;background:radial-gradient(ellipse at 55% 65%,#e8342a 0%,#c21f18 45%,#5a5a5a 70%,#fff 100%)}
.services{position:absolute;left:709px;top:622px}
.services h2{font-size:28px;margin-bottom:16px}
.services li{list-style:none;font-size:19px;line-height:22px}
.testimonials{position:absolute;left:499px;top:845px;width:452px}
.testimonials h2{font-size:27px;margin-bottom:14px}
.testimonials p{font-size:17.4px;line-height:20px;text-align:justify;text-indent:33px}
.testimonials cite{display:block;text-align:right;font-family:"Mulish",sans-serif;font-style:italic;font-size:15px;margin-top:10px}
</style>
</head>
<body>
<div class="backdrop" role="img" aria-label="Blurred canola field under a blue sky"></div>

<main class="page-card">
  <div class="card-top"></div>
  <div class="hero" role="img" aria-label="Farmer walking through a blooming yellow canola field under a cloudy blue sky"></div>

  <div class="mission">
    <p>We are a pump an compressor repair facility in Alberta Canada. Dummy Text. This may contain the main vision / goal / objective of the company.</p>
    <span class="more">...see more</span>
  </div>
  <form class="search">
    <input type="text" placeholder="Search model or product name" aria-label="Search">
    <button type="button">Search</button>
  </form>

  <section class="welcome">
    <h2>Welcome to Zamo Rotating Solutions</h2>
    <p>Dummy Text. This section may content basic information about the com pany. This following is a dummy text. Ultimately, our goal is to help you keep your plant/facility running smoothly and efficiently. We understand the requirements necessary to meet your demands. With over 100 years of combined mechanical expertise, our Service Staff has the experience to handle your needs.</p>
    <p>All Ridgeline Pump &amp; Compressor Technicians undergo in-depth training by many of our manufacturers throughout their careers at Ridgeline Pump &amp; Compressor. Product training is ongoing to keep up with the many updates and technical improvements in our industry which are critical to providing you, the customer, with the expert level of service that you deserve.</p>
    <span class="see-more">...see more</span>
  </section>

  <figure class="product-photo"><div role="img" aria-label="Red portable air compressor"></div></figure>

  <section class="services">
    <h2>Services Offered:</h2>
    <ul>
      <li>-Pump Repairs</li><li>-Pump Repairs</li><li>-Pump Repairs</li><li>-Pump Repairs</li><li>-Pump Repairs</li>
      <li>-Dummy Text Services</li><li>-Dummy Text Services</li>
    </ul>
  </section>

  <section class="testimonials">
    <h2>Testimonials</h2>
    <p>Dummy Text Sample. I have been extremely impressed with Brightline Works. In a highly specialized medical device industry, they seized quickly on the opportunities and issues in our business and put together a comprehensive plan.</p>
    <cite>-Multi-hectare farm owner:Marla Dufresne</cite>
  </section>
</main>

<div class="logo-box">
  <span class="logo-mark"></span>
  <span class="logo-name">ZAMO</span>
  <span class="logo-tag">ROTATING SOLUTIONS</span>
</div>

<div class="contact phone">
  <svg width="16" height="20" viewBox="0 0 16 20"><path d="M4 1 L7 1 L8 6 L6 7.5 Q7 12 10 14.5 L12 13 L15 16 L13.5 19 Q6 18 2.5 10 Q1 5 4 1Z" fill="#333"/></svg>
  (555)014-2290
</div>
<div class="contact email">
  <svg width="28" height="19" viewBox="0 0 28 19"><rect x="0.5" y="0.5" width="27" height="18" fill="#333"/><path d="M1 1 L14 11 L27 1 M1 18 L10 8 M27 18 L18 8" stroke="#fff" stroke-width="1.4" fill="none"/></svg>
  hello@zamo-example.com
</div>

<nav class="main-nav">
  <a href="#" class="active">HOME</a>
  <a href="#">ABOUT US</a>
  <a href="#">SERVICES</a>
  <a href="#">CONTACT US</a>
</nav>
</body>
</html>
```